Visitenkarten-Design für Hotel und Restaurant in der Fußgängerzone
Zielgruppe
Hotel und Restaurant in der Fußgängerzone, zwei Gehminuten zum Bodensee.
Neu renoviertes Hotel/Restaurant (z.B.Boxspringbett, Holzboden, USB Steckdosen).
Übernachtung mit Frühstück im Einzel,-Doppel,- oder Komfortzimmer (für 3 Personen).
Restaurant mit regionaler Küche. Besondere saisonale Zutaten unserer Nachbarländer als Specials.
Touristen im Sommer Durchschnittalter: 50 Jahre, sportlich, modern, gut betucht.
Einwohner der Stadt im Winter, Alter zwischen 25 und 65 Jahre, viele davon Hausbesitzer, Segelboot Besitzer etc.
Aufgabenstellung
Farbkonzept im Restaurant:
warm- weiße Wände, dunkle Holzmöbel, rote Barelemente, weiß-kupferfarbene Lampen.
Würden uns etwas minimalistisches wünschen, trotzdem mit einem Wow Effekt.
Sei es ein ausgeschnittenes Logo, abgerundete Ecken, besonderes Material usw.
Dateianhänge sind nur für´s bessere Verständnis, muss nicht zwingend als Vorgabe gesehen werden.
Vorderseite:
Logo
Hotel & Restaurant (kann, muss aber nicht draufstehen.)
zum Anker
Mühlbach

```html
<!DOCTYPE html>
<html lang="de">
<head>
<meta charset="utf-8">
<title>zum Anker – Visitenkarte</title>
<link href="https://fonts.googleapis.com/css2?family=Josefin+Sans:wght@300;400;600&display=swap" rel="stylesheet">
<style>
  :root{
    --stage:#e8e5e1;
    --card:#1d1d1c;
    --gold:#c9a24a;
    --gold-light:#f1d78a;
    --gold-dark:#8a6422;
    --mark:#d9d4cc;
    --mark-copper:#5a3e2b;
    --text-light:#e6e1d8;
  }
  *{box-sizing:border-box;margin:0;padding:0}
  html,body{width:1200px;height:758px;overflow:hidden;background:var(--stage)}
  body{font-family:"Josefin Sans",sans-serif;position:relative}
  .card{
    position:absolute;top:209px;width:540px;height:340px;padding:6px;
    background:linear-gradient(135deg,var(--gold-dark),var(--gold-light) 35%,var(--gold) 55%,var(--gold-dark) 80%,var(--gold-light));
    border-radius:8px 44px 8px 44px;
  }
  .card--front{left:40px}
  .card--back{left:620px}
  .card__face{
    width:100%;height:100%;background:var(--card);position:relative;
    border-radius:4px 38px 4px 38px;overflow:hidden;
  }
  .front__mark{
    position:absolute;left:50%;top:58px;width:112px;height:112px;margin-left:-56px;
    border-radius:50%;background:var(--mark);
  }
  .front__name{
    position:absolute;left:0;right:0;top:196px;text-align:center;
    color:var(--gold);font-weight:600;font-size:38px;letter-spacing:.5px;
  }
  .front__city{
    position:absolute;left:0;right:0;top:252px;display:flex;justify-content:center;align-items:center;gap:10px;
    color:var(--gold);font-weight:300;font-size:14px;letter-spacing:2px;
  }
  .front__city::before,.front__city::after{content:"";width:40px;height:1px;background:var(--gold)}
  .back__mark{
    position:absolute;left:50%;top:40px;width:112px;height:112px;margin-left:-56px;
    border-radius:50%;background:var(--mark-copper);
  }
  .back__name{
    position:absolute;left:72px;top:178px;color:var(--gold);font-size:19px;font-weight:300;
  }
  .contact{position:absolute;display:flex;align-items:flex-start;gap:10px;color:var(--text-light);font-size:14px;font-weight:300;line-height:19px;white-space:nowrap}
  .contact svg{width:13px;height:13px;margin-top:2px;flex:none}
  .contact--address{left:50px;top:228px}
  .contact--phone{left:50px;top:282px}
  .contact--mail{left:278px;top:238px}
  .contact--web{left:278px;top:282px}
</style>
</head>
<body>
  <div class="card card--front">
    <div class="card__face">
      <div class="front__mark"></div>
      <div class="front__name">zum Anker</div>
      <div class="front__city">Mühlbach</div>
    </div>
  </div>

  <div class="card card--back">
    <div class="card__face">
      <div class="back__mark"></div>
      <div class="back__name">Zum Anker</div>

      <div class="contact contact--address">
        <svg viewBox="0 0 12 12"><path d="M6 0.5a4 4 0 0 0-4 4c0 3 4 7 4 7s4-4 4-7a4 4 0 0 0-4-4zm0 5.5a1.5 1.5 0 1 1 0-3 1.5 1.5 0 0 1 0 3z" fill="#c9a24a"/></svg>
        <span>Seestraße 12<br>78199 Mühlbach</span>
      </div>
      <div class="contact contact--phone">
        <svg viewBox="0 0 12 12"><path d="M2.5 0.8l2 0.2 1 2.6-1.3 1a6.5 6.5 0 0 0 3.2 3.2l1-1.3 2.6 1 .2 2c-.3.9-1.2 1.3-2 1.2C5 10.3 1.7 7 1.3 3c-.1-.9.3-1.8 1.2-2.2z" fill="#c9a24a"/></svg>
        <span>075 510 482 17</span>
      </div>
      <div class="contact contact--mail">
        <svg viewBox="0 0 12 12"><rect x="0.8" y="2.3" width="10.4" height="7.4" fill="none" stroke="#c9a24a" stroke-width="1"/><path d="M1 2.6l5 4 5-4" fill="none" stroke="#c9a24a" stroke-width="1"/></svg>
        <span>info@zum-anker-hotel.de</span>
      </div>
      <div class="contact contact--web">
        <svg viewBox="0 0 12 12"><circle cx="6" cy="6" r="5.2" fill="none" stroke="#c9a24a" stroke-width="1"/><ellipse cx="6" cy="6" rx="2.3" ry="5.2" fill="none" stroke="#c9a24a" stroke-width="1"/><path d="M0.8 6h10.4M1.6 3.5h8.8M1.6 8.5h8.8" stroke="#c9a24a" stroke-width="0.8"/></svg>
        <span>www.zum-anker-hotel.de</span>
      </div>
    </div>
  </div>
</body>
</html>
```